Spring Savings Package for The Lodge at Marlow's Landing Lodge

Design an email and elevator poster 11x7 that promotes Spring and our heated pools at The Lodge at Marlow's Landing
Text-

Worried about the Spring Weather don't #IndoorWaterpark !

Ask about our Springtime Savings that comes with a Free Resort Beach Towel ($12 value).

Book by March 1st,2019
Stay Dates Now-May 23rd,2019

Phone number: 800.555.0172

Reserve Now! www (dot) lodgeatmarlowslanding-example (dot) com

Target Market(s)

Guest reserving Spring Break

Industry/Entity Type

Hospitality

Requirements
Must have
• text
• phone
• website
• Book Now
• Can change some of the text to make it more of a Sales piece
Nice to have
• Brand Colors

```html
<!DOCTYPE html>
<html lang="en">
<head>
<meta charset="utf-8">
<title>Spring Savings – The Lodge at Marlow's Landing</title>
<link rel="stylesheet" href="https://fonts.googleapis.com/css2?family=Tinos:wght@400;700&family=Yanone+Kaffeesatz:wght@600&family=Kaushan+Script&family=Fondamento&family=Roboto+Condensed:wght@700&display=swap">
<style>
:root{
  --frame:#7a7c79;
  --white:#ffffff;
  --navy:#262f6e;
  --body-grey:#555555;
  --tan:#d4a05a;
  --gold-title:#f1c21b;
  --panel:#efefef;
  --pink:#d6197a;
  --pink-bg:#fde6f2;
  --gold:#d9a11b;
  --gold-bg:#fdf0c8;
  --blue:#1a6ec7;
  --blue-bg:#e6f3fd;
}
*{box-sizing:border-box;margin:0;padding:0}
html,body{width:1200px;height:2441px;overflow:hidden;background:var(--frame)}
.email{position:absolute;left:29px;top:20px;width:1148px;height:2397px;background:var(--white);font-family:"Tinos",serif}
.header{position:absolute;left:0;top:0;width:1148px;height:207px}
.brand-name{position:absolute;left:22px;top:62px;width:300px;font-family:"Tinos",serif;font-weight:700;font-size:31px;line-height:38px;color:var(--navy)}
.header-phone{position:absolute;right:24px;top:114px;font-family:"Tinos",serif;font-weight:700;font-size:33px;color:var(--navy);letter-spacing:1px}
.nav{position:absolute;left:0;top:207px;width:1148px;height:61px;background:var(--navy);display:flex;align-items:center}
.nav span{color:var(--white);font-family:"Tinos",serif;font-size:28px;text-transform:uppercase;position:absolute;top:14px}
.hero{position:absolute;left:0;top:268px;width:1148px;height:668px;overflow:hidden}
.hero-photo{position:absolute;inset:0;background:linear-gradient(180deg,#3a3f86 0%,#6c5a8c 22%,#c88d6a 36%,#d98a3a 50%,#4f87a8 66%,#5fb5d8 78%,#7c8a86 100%)}
.hero-kicker{position:absolute;left:70px;top:28px;font-family:"Yanone Kaffeesatz",sans-serif;font-weight:600;font-size:64px;letter-spacing:2px;color:var(--gold-title)}
.hero-script{position:absolute;left:250px;top:80px;font-family:"Kaushan Script",cursive;font-size:100px;color:var(--white)}
.hero-wave{position:absolute;left:0;bottom:0}
.intro{position:absolute;left:0;top:1000px;width:1148px;text-align:center}
.intro h1{font-family:"Tinos",serif;font-weight:700;font-size:43px;line-height:54px;color:var(--navy);letter-spacing:1px}
.intro p{margin:22px auto 0;width:900px;font-size:28px;line-height:47px;color:var(--body-grey)}
.offers{position:absolute;left:0;top:1326px;width:1148px;height:559px;display:flex;gap:5px}
.offer{flex:1;position:relative}
.offer.spring{background:var(--pink-bg);color:var(--pink)}
.offer.fall{background:var(--gold-bg);color:var(--gold)}
.offer.summer{background:var(--blue-bg);color:var(--blue)}
.offer-title{position:absolute;top:24px;width:100%;text-align:center;font-family:"Fondamento",cursive;font-size:54px;line-height:50px}
.offer-title .small{font-size:48px;display:block}
.offer-photo{position:absolute;left:0;top:150px;width:100%;height:267px}
.spring .offer-photo{background:linear-gradient(180deg,#c6b08a,#e8d25a 45%,#8ec9d8)}
.fall .offer-photo{background:linear-gradient(180deg,#8bb0d8,#c08a55 40%,#3da8c8)}
.summer .offer-photo{background:linear-gradient(180deg,#d8d2c8,#9bb9c8 55%,#c8e0e8)}
.offer-save{position:absolute;top:455px;width:100%;display:flex;justify-content:center;align-items:flex-start;font-family:"Roboto Condensed",sans-serif;font-weight:700}
.offer-save .label{font-size:38px;line-height:36px;text-align:center;margin-top:10px}
.offer-save .pct{font-size:84px;line-height:84px;margin-left:8px}
.offer-save .pct sup{font-size:44px;vertical-align:top;position:relative;top:4px}
.booking{position:absolute;left:0;top:1901px;width:1148px;height:339px;background:var(--panel);text-align:center;color:var(--navy)}
.booking p{font-size:34px;line-height:55px}
.booking .lines{padding-top:40px}
.reserve{position:absolute;left:380px;top:227px;width:322px;height:77px;background:var(--navy);color:var(--white);font-weight:700;font-size:29px;display:flex;align-items:center;justify-content:center}
.footer{position:absolute;left:0;top:2240px;width:1148px;height:157px;background:var(--tan);text-align:center;color:var(--white)}
.footer .url{padding-top:40px;font-size:33px}
.footer .copy{margin-top:10px;font-size:21px}
</style>
</head>
<body>
<div class="email">
  <header class="header">
    <div class="brand-name">The Lodge at<br>Marlow's Landing</div>
    <div class="header-phone">CELL: 800.555.0172</div>
  </header>
  <nav class="nav">
    <span style="left:55px">Guest Rooms</span>
    <span style="left:338px">Waterpark</span>
    <span style="left:592px">Discounts</span>
    <span style="left:878px">Recreation</span>
  </nav>
  <section class="hero">
    <div class="hero-photo" role="img" aria-label="Lodge buildings surrounding an outdoor pool with colourful water slides at dusk"></div>
    <div class="hero-kicker">FAMILY VACATION MEETS....</div>
    <div class="hero-script">Fun &amp; Relaxation</div>
    <svg class="hero-wave" width="1148" height="668" viewBox="0 0 1148 668">
      <path d="M0,565 C250,530 480,640 760,640 C960,640 1080,580 1148,470 L1148,668 L0,668Z" fill="var(--tan)"/>
      <path d="M0,590 C250,555 480,668 760,668 L0,668Z" fill="var(--white)"/>
    </svg>
  </section>
  <section class="intro">
    <h1>WORRIED ABOUT THE WEATHER<br>DON'T #HEATEDPOOLS !</h1>
    <p>Ask about our Springtime Savings that comes with a Free Willow Falls Waterpark Lodge Beach Towel ($12 value). PLUS! A Mountain Breakfast at Hearthside Kitchen is included with all stays.</p>
  </section>
  <section class="offers">
    <div class="offer spring">
      <div class="offer-title"><span class="small">Spring</span>Savings</div>
      <div class="offer-photo" role="img" aria-label="Kids splashing out of a yellow water slide"></div>
      <div class="offer-save"><div class="label">Save<br>up to</div><div class="pct">20<sup>%</sup></div></div>
    </div>
    <div class="offer fall">
      <div class="offer-title"><span class="small">Fall</span>Savings</div>
      <div class="offer-photo" role="img" aria-label="Group of kids on an inflatable tube in the pool"></div>
      <div class="offer-save"><div class="label">Save<br>up to</div><div class="pct">30<sup>%</sup></div></div>
    </div>
    <div class="offer summer">
      <div class="offer-title"><span class="small">Summer</span>Savings</div>
      <div class="offer-photo" role="img" aria-label="Children walking through an indoor splash area"></div>
      <div class="offer-save"><div class="label">Save<br>up to</div><div class="pct">35<sup>%</sup></div></div>
    </div>
  </section>
  <section class="booking">
    <div class="lines">
      <p>Book by March 1st,2019</p>
      <p>Stay Dates Now-May 23rd,2019</p>
      <p>Phone number: 800.555.0172</p>
    </div>
    <div class="reserve">RESERVE NOW!</div>
  </section>
  <footer class="footer">
    <div class="url">www.lodgeatmarlowslanding-example.com</div>
    <div class="copy">Copyright @ 2019 lodgeatmarlowslanding-example.com</div>
  </footer>
</div>
</body>
</html>
```